Craft oriented film company needs a Business Card design

Hi all,
We're a 2-man band film company in New Zealand called Kestrel Pictures. We're good honest blokes, who are very passionate about the craft of film making. I've attached our current logo which has a bit of a crafty/artisan feel that we like. Feel free to use it - or throw the baby out with the bathwater and start again..... you never know, you might inspire a complete brand re-work.

In any case, the vibe we want to give out is that we are solid, dependable and no bullshit - but without compromising creative excellence and being in the now. We like the 'Brooklyn' artisan style of work.

Preferably single sided.

We need the standard stuff:
Name, job title, cellphone, email address and physical address (this can be smaller if you like - street, suburb, city & zip, country [if you want])

Check out our website to learn more about us: kestrelpictures.example

Target Market(s)

Brand marketers and advertising agency creatives looking for video production.

Industry/Entity Type

Baby

Requirements
Should not have
• Nothing flashy or too 'futuristic', we want it to feel grounded and real. A limited colour palette is preferred.
We don't want any film reels or cameras or anything obvious like that.

```html
<!DOCTYPE html>
<html lang="en">
<head>
<meta charset="utf-8">
<title>Kestrel Pictures — Business Cards</title>
<link href="https://fonts.googleapis.com/css2?family=Arvo:wght@700&family=Dosis:wght@500;600&family=Yellowtail&display=swap" rel="stylesheet">
<style>
  :root {
    --page: #000000;
    --card: #ffffff;
    --ink: #1f1d1e;
    --accent: #c4232f;
    --hatch: #d9d9d9;
    --dots: #2a2a2a;
  }
  html, body {
    margin: 0;
    padding: 0;
    width: 1200px;
    height: 1000px;
    overflow: hidden;
    background: var(--page);
  }
  .sheet {
    position: relative;
    width: 1200px;
    height: 1000px;
  }
  .card {
    position: absolute;
    top: 40px;
    width: 552px;
    height: 911px;
    background: var(--card);
    color: var(--ink);
    font-family: "Dosis", sans-serif;
    font-weight: 500;
  }
  .card--producer { left: 37px; }
  .card--director { left: 614px; }

  .brand-field {
    position: absolute;
    left: 20px;
    top: 20px;
    width: 512px;
    height: 385px;
    background: var(--hatch);
  }
  .brand-name {
    position: absolute;
    left: 20px;
    top: 20px;
    width: 512px;
    height: 385px;
    display: flex;
    align-items: center;
    justify-content: center;
    gap: 16px;
    font-family: "Dosis", sans-serif;
    font-weight: 600;
    font-size: 46px;
    letter-spacing: 2px;
    text-transform: uppercase;
    color: var(--ink);
  }
  .brand-dot {
    width: 22px;
    height: 22px;
    border-radius: 50%;
    background: var(--ink);
  }

  .person {
    position: absolute;
    left: 0;
    width: 552px;
    top: 478px;
    text-align: center;
    font-family: "Arvo", serif;
    font-weight: 700;
    font-size: 50px;
    letter-spacing: 9px;
    line-height: 1;
    margin: 0;
  }
  .role {
    position: absolute;
    top: 530px;
    left: 0;
    width: 552px;
    text-align: center;
    font-family: "Yellowtail", cursive;
    font-size: 30px;
    color: var(--accent);
    line-height: 1;
    transform: rotate(-6deg);
  }

  .rule {
    position: absolute;
    left: 20px;
    width: 508px;
    height: 0;
    border-top: 3px dotted var(--dots);
  }
  .rule--1 { top: 593px; }
  .rule--2 { top: 705px; }
  .rule--3 { top: 816px; }

  .contact-row {
    position: absolute;
    top: 618px;
    left: 20px;
    width: 510px;
    height: 62px;
  }
  .phone {
    position: absolute;
    left: 0;
    width: 234px;
    top: 0;
    line-height: 62px;
    font-size: 23px;
    letter-spacing: 1px;
    text-align: left;
  }
  .phone .mark { color: var(--accent); }
  .divider {
    position: absolute;
    left: 235px;
    top: 2px;
    height: 58px;
    border-left: 3px dotted var(--dots);
  }
  .email {
    position: absolute;
    right: 0;
    top: 0;
    line-height: 62px;
    font-size: 19px;
    text-align: right;
  }
  .email .mark { color: var(--accent); }

  .address {
    position: absolute;
    top: 725px;
    left: 0;
    width: 552px;
    text-align: center;
    font-size: 24px;
    line-height: 39px;
    margin: 0;
  }
  .address .sep {
    color: var(--accent);
    font-size: 18px;
    padding: 0 4px;
  }
  .web {
    position: absolute;
    top: 844px;
    left: 0;
    width: 552px;
    text-align: center;
    font-size: 24px;
    margin: 0;
  }
  .web .host { color: var(--accent); }
</style>
</head>
<body>
<main class="sheet">

  <article class="card card--producer">
    <div class="brand-field" role="img" aria-label="Diagonal hatched line pattern behind the company name"></div>
    <div class="brand-name"><span class="brand-dot"></span>Kestrel Pictures</div>
    <h1 class="person">ROWAN TEPPER</h1>
    <p class="role">producer</p>
    <div class="rule rule--1"></div>
    <div class="contact-row">
      <div class="phone"><span class="mark">{</span>+64<span class="mark">.</span>21<span class="mark">.</span>555<span class="mark">.</span>017<span class="mark">}</span></div>
      <div class="divider"></div>
      <div class="email">rowan<span class="mark">@</span>kestrelpictures.example</div>
    </div>
    <div class="rule rule--2"></div>
    <p class="address">14 Harlow St <span class="sep">›‹</span> Kingsland<br>Auckland <span class="sep">›‹</span> New Zealand 1024</p>
    <div class="rule rule--3"></div>
    <p class="web">http://<span class="host">www.kestrelpictures.example</span></p>
  </article>

  <article class="card card--director">
    <div class="brand-field" role="img" aria-label="Diagonal hatched line pattern behind the company name"></div>
    <div class="brand-name"><span class="brand-dot"></span>Kestrel Pictures</div>
    <h1 class="person">HUGH CALDER</h1>
    <p class="role">director</p>
    <div class="rule rule--1"></div>
    <div class="contact-row">
      <div class="phone"><span class="mark">{</span>+64<span class="mark">.</span>21<span class="mark">.</span>55<span class="mark">.</span>3000<span class="mark">}</span></div>
      <div class="divider"></div>
      <div class="email">hugh<span class="mark">@</span>kestrelpictures.example</div>
    </div>
    <div class="rule rule--2"></div>
    <p class="address">14 Harlow St <span class="sep">›‹</span> Kingsland<br>Auckland <span class="sep">›‹</span> New Zealand 1024</p>
    <div class="rule rule--3"></div>
    <p class="web">http://<span class="host">www.kestrelpictures.example</span></p>
  </article>

</main>
</body>
</html>
```